Interior designer needs a gorgeous, chic business card design.

A new, small Interior Design firm needs a business card that is chic, contemporary and elegant. Nothing over the top. My interiors are contemporary classic with an elegant feel to them. I like to use quality finishes and products rather than follow the latest fads. Projects can be anything from Pre start selections, bathrooms, kitchens, bedrooms, custom upholstery, furniture, rugs and art etc. The final design should display quality and an achievable sense of chic. I am open to all colours including black but not limited to this.

```html
<!DOCTYPE html>
<html lang="en">
<head>
<meta charset="utf-8">
<title>Interior Design Business Card</title>
<link rel="stylesheet" href="https://fonts.googleapis.com/css2?family=Jost:wght@700&family=Fjalla+One&display=swap">
<style>
  :root {
    --page: #ffffff;
    --teal: #14a79c;
    --ink: #111111;
    --paper: #ffffff;
    --backdrop-light: #f4f4f4;
    --backdrop-dark: #c9c9c9;
  }
  * { box-sizing: border-box; margin: 0; padding: 0; }
  html, body { width: 1200px; height: 900px; overflow: hidden; background: var(--page); }
  .canvas { position: relative; width: 1200px; height: 900px; }

  .presentation-panel {
    position: absolute;
    background: radial-gradient(ellipse at 50% 55%, var(--backdrop-light) 0%, #e6e6e6 55%, var(--backdrop-dark) 100%);
  }
  .panel-front { left: 291px; top: 72px; width: 626px; height: 358px; }
  .panel-back  { left: 289px; top: 462px; width: 628px; height: 359px; }

  .cut-line {
    position: absolute;
    width: 455px; height: 239px;
    border: 2px dashed var(--teal);
    border-radius: 36px;
  }
  .card {
    position: absolute;
    width: 445px; height: 225px;
    border: 6px solid var(--ink);
    border-radius: 30px;
    display: flex; flex-direction: column; align-items: center; justify-content: center;
  }
  .cut-front { left: 376px; top: 131px; }
  .card-front { left: 381px; top: 139px; background: var(--paper); }
  .cut-back  { left: 375px; top: 521px; }
  .card-back { left: 380px; top: 528px; background: var(--teal); }

  .holder-name {
    font-family: "Jost", "Futura", sans-serif;
    font-weight: 700;
    font-size: 41px;
    letter-spacing: 1px;
    line-height: 1;
    color: var(--ink);
    padding-bottom: 6px;
    border-bottom: 2px dashed var(--teal);
    margin-top: -2px;
  }
  .holder-title {
    font-family: "Fjalla One", "Arial Narrow", sans-serif;
    font-size: 23px;
    line-height: 1;
    color: var(--ink);
    margin-top: 5px;
    letter-spacing: 0.3px;
  }
  .contact-list {
    list-style: none;
    text-align: center;
    font-family: "Fjalla One", "Arial Narrow", sans-serif;
    font-size: 20px;
    line-height: 26px;
    color: var(--paper);
    letter-spacing: 0.3px;
    margin-top: -5px;
  }
</style>
</head>
<body>
<main class="canvas">
  <div class="presentation-panel panel-front" role="img" aria-label="Soft grey backdrop with pale polka dots"></div>
  <div class="presentation-panel panel-back" role="img" aria-label="Soft grey backdrop with pale polka dots"></div>

  <div class="cut-line cut-front"></div>
  <section class="card card-front">
    <h1 class="holder-name">YOUR NAME HERE</h1>
    <p class="holder-title">interior design master</p>
  </section>

  <div class="cut-line cut-back"></div>
  <section class="card card-back">
    <ul class="contact-list">
      <li>This is the address</li>
      <li>This is the phone number</li>
      <li>This is the website</li>
    </ul>
  </section>
</main>
</body>
</html>
```